serious, thorough, light and simple - that's my advice and mediations

My business card should combine my logo (uploaded file) and my homepage (https://fellor-mediation.webnestsite.com).

Contact Information for Business Card

Name: Sabine Fellor di Vanti
Phone: 076 412 58 94
mail: sfellor@postkiv.ch
web: www.fellor-di-vanti.ch

```html
<!DOCTYPE html>
<html lang="de">
<head>
<meta charset="utf-8">
<title>Visitenkarte – Sabine Fellor di Vanti</title>
<link href="https://fonts.googleapis.com/css2?family=Roboto:wght@400;500&display=swap" rel="stylesheet">
<style>
  :root {
    --backdrop: #e2e2e0;
    --card-white: #ffffff;
    --gold: #a8824a;
    --green: #1d6b45;
    --grad-top: #176a45;
    --grad-bottom: #233f84;
    --white: #ffffff;
  }
  html, body {
    margin: 0;
    padding: 0;
    width: 1125px;
    height: 1200px;
    overflow: hidden;
    background: var(--backdrop);
    font-family: "Roboto", Arial, sans-serif;
  }
  .canvas {
    position: relative;
    width: 1125px;
    height: 1200px;
  }
  .card {
    position: absolute;
    left: 150px;
    width: 825px;
    height: 472px;
    border-radius: 24px;
    overflow: hidden;
  }
  .card--front {
    top: 98px;
    background: var(--card-white);
  }
  .card--back {
    top: 631px;
    background: linear-gradient(180deg, var(--grad-top) 0%, var(--grad-bottom) 100%);
  }

  /* Brand: invented name set in the card's text font */
  .brand {
    position: absolute;
    margin: 0;
    font-weight: 500;
    white-space: nowrap;
    line-height: 1;
  }
  .card--front .brand {
    left: 108px;
    width: 258px;
    top: 192px;
    text-align: center;
    font-size: 32px;
    color: var(--gold);
  }
  .card--back .brand {
    left: 0;
    right: 0;
    top: 170px;
    text-align: center;
    font-size: 60px;
    color: var(--white);
  }

  .divider {
    position: absolute;
    left: 412px;
    top: 147px;
    width: 2px;
    height: 176px;
    background: var(--green);
  }
  .contact {
    position: absolute;
    left: 450px;
    top: 155px;
  }
  .contact__name {
    margin: 0 0 30px;
    font-size: 27px;
    font-weight: 500;
    color: var(--gold);
  }
  .contact__list {
    list-style: none;
    margin: 0;
    padding: 0;
  }
  .contact__item {
    display: flex;
    align-items: center;
    gap: 14px;
    height: 33px;
    font-size: 22px;
    color: var(--green);
  }
  .contact__icon {
    width: 18px;
    height: 18px;
    flex: none;
  }
  .accent { color: var(--gold); }

  .back-web {
    position: absolute;
    left: 0;
    right: 0;
    top: 412px;
    margin: 0;
    line-height: 24px;
    text-align: center;
    font-size: 21px;
    color: var(--white);
  }
</style>
</head>
<body>
<div class="canvas">

  <section class="card card--front" aria-label="Vorderseite">
    <p class="brand">Wege im Dialog</p>
    <div class="divider"></div>
    <div class="contact">
      <p class="contact__name">Sabine Fellor di Vanti</p>
      <ul class="contact__list">
        <li class="contact__item">
          <svg class="contact__icon" viewBox="0 0 24 24" aria-hidden="true">
            <path fill="#a8824a" d="M6.6 10.8a15.1 15.1 0 0 0 6.6 6.6l2.2-2.2a1 1 0 0 1 1-.25 11.4 11.4 0 0 0 3.6.57 1 1 0 0 1 1 1V20a1 1 0 0 1-1 1A17 17 0 0 1 3 4a1 1 0 0 1 1-1h3.5a1 1 0 0 1 1 1c0 1.25.2 2.450.57 3.57a1 1 0 0 1-.25 1z"/>
          </svg>
          <span>076 412 58 94</span>
        </li>
        <li class="contact__item">
          <svg class="contact__icon" viewBox="0 0 24 24" aria-hidden="true">
            <rect x="2.5" y="5" width="19" height="14" rx="1.5" fill="none" stroke="#a8824a" stroke-width="2"/>
            <path d="M3 6l9 7 9-7" fill="none" stroke="#a8824a" stroke-width="2"/>
          </svg>
          <span>sfellor@postkiv.ch</span>
        </li>
        <li class="contact__item">
          <svg class="contact__icon" viewBox="0 0 24 24" aria-hidden="true">
            <g fill="none" stroke="#a8824a" stroke-width="1.8">
              <circle cx="12" cy="12" r="9.5"/>
              <ellipse cx="12" cy="12" rx="4.2" ry="9.5"/>
              <path d="M2.5 12h19M4 7h16M4 17h16"/>
            </g>
          </svg>
          <span>www.<span class="accent">fellor-di-vanti</span>.ch</span>
        </li>
      </ul>
    </div>
  </section>

  <section class="card card--back" aria-label="Rückseite">
    <p class="brand">Wege im Dialog</p>
    <p class="back-web">www.fellor-di-vanti.ch</p>
  </section>

</div>
</body>
</html>
```